Volquen Business Card

I have a business that is called "Volquen Electrical Products LTD" My company deals with top of the range laptops and mobile phones that are exclusive. I need a business card that will be eye catching but not over complicated.

Target Market(s)

Adults aged 19 to 50
Upper middle class

Industry/Entity Type

Business

Requirements
Must have
• Company name/logo (file attached)
• It must have my contact information which is:

• Name: Dale Marwick

• Position: Managing Director 

• Business Address: 7 Hapton Row, London, W4 9QD

• Contact Number: 02085193604
• Mobile: 07814260537
• Email: info@volquen-goods.co.uk
Nice to have
• Simple and stylish
• Eye catching

```html
<!DOCTYPE html>
<html lang="en">
<head>
<meta charset="utf-8">
<title>Volquen Business Card</title>
<link rel="stylesheet" href="https://fonts.googleapis.com/css2?family=Arvo:ital,wght@0,700;1,700&family=Zilla+Slab:wght@300&family=Questrial&display=swap">
<style>
  :root {
    --backdrop: #1c1c1d;
    --card-front-light: #505254;
    --card-front-mid: #3a3c3e;
    --card-front-dark: #2a2b2d;
    --card-back: #050505;
    --brand-blue: #1cb4e4;
    --title-blue: #3a9fd0;
    --tagline-blue: #3b7eae;
    --name-white: #ffffff;
    --detail-grey: #e4e4e4;
  }
  * { margin: 0; padding: 0; box-sizing: border-box; }
  html, body { width: 1200px; height: 720px; overflow: hidden; background: var(--backdrop); }
  .stage {
    width: 1200px;
    height: 720px;
    display: flex;
    align-items: center;
    justify-content: center;
    gap: 40px;
  }
  .card {
    position: relative;
    width: 540px;
    height: 330px;
    border-radius: 3px;
    overflow: hidden;
    box-shadow: 0 6px 18px rgba(0, 0, 0, 0.5);
  }
  .card--front {
    background: radial-gradient(ellipse at 72% 32%, var(--card-front-light) 0%, var(--card-front-mid) 45%, var(--card-front-dark) 100%);
  }
  .card--back {
    background: radial-gradient(ellipse at 50% 40%, #151617 0%, var(--card-back) 80%);
  }
  .brand-mark {
    position: absolute;
    top: 48px;
    right: 40px;
    display: flex;
    align-items: center;
    gap: 12px;
    font-family: "Questrial", sans-serif;
    font-size: 36px;
    line-height: 1;
    color: var(--brand-blue);
    letter-spacing: 1px;
  }
  .brand-mark__dot {
    width: 22px;
    height: 22px;
    border-radius: 50%;
    background: var(--brand-blue);
  }
  .contact {
    position: absolute;
    left: 40px;
    bottom: 30px;
  }
  .contact__name {
    font-family: "Arvo", serif;
    font-weight: 700;
    font-size: 36px;
    color: var(--name-white);
    line-height: 1.1;
  }
  .contact__role {
    font-family: "Arvo", serif;
    font-weight: 700;
    font-style: italic;
    font-size: 21px;
    line-height: 1.3;
    color: var(--title-blue);
    margin-bottom: 2px;
  }
  .contact__line {
    font-family: "Zilla Slab", serif;
    font-weight: 300;
    font-size: 22px;
    color: var(--detail-grey);
    line-height: 1.3;
    white-space: nowrap;
  }
  .contact__phones { display: flex; gap: 44px; }
  .logo-lockup {
    position: absolute;
    inset: 0;
    display: flex;
    flex-direction: column;
    align-items: center;
    justify-content: center;
  }
  .logo-lockup__name {
    font-family: "Questrial", sans-serif;
    font-size: 92px;
    color: var(--brand-blue);
    letter-spacing: 4px;
    line-height: 1;
  }
  .logo-lockup__tagline {
    font-family: "Questrial", sans-serif;
    font-size: 32px;
    color: var(--tagline-blue);
    letter-spacing: 3px;
    margin-top: 10px;
  }
</style>
</head>
<body>
<main class="stage">
  <section class="card card--front" aria-label="Business card front">
    <div class="brand-mark"><span class="brand-mark__dot"></span>Volquen</div>
    <div class="contact">
      <p class="contact__name">Dale Marwick</p>
      <p class="contact__role">Managing Director</p>
      <p class="contact__line">7 Hapton Row, London, W4 9QD</p>
      <p class="contact__line contact__phones"><span>02085193604</span><span>M:07814260537</span></p>
      <p class="contact__line">info@volquen-goods.co.uk</p>
    </div>
  </section>
  <section class="card card--back" aria-label="Business card back">
    <div class="logo-lockup">
      <p class="logo-lockup__name">VOLQUEN</p>
      <p class="logo-lockup__tagline">Electrical Products</p>
    </div>
  </section>
</main>
</body>
</html>
```